Cambodia 501c3 flyer design

I need a flyer to build interest and awareness for a school year kick off event in October for our charity school in rural Cambodia. I have text and photos available and just need help getting a professional look and feel. (Other projects may follow, including logo and web redesign.)

Founded in 2004 by Lars Trulsen, The Riverside Learning House at Prek Sala is a 501(c)(3) organization dedicated to breaking the cycle of poverty of some of Cambodia's poorest children by providing a rigorous core K-9 education that emphasizes English proficiency.

"The board of directors of The Riverside Learning House at Prek Sala invites you to our annual visit to Prek Sala, Cambodia to help launch the new school year. The trip is open to everyone-you do not need to be a current donor to attend.

If you have been interested in visiting an educational project that works for hundreds of the poorest children in Cambodia, here is your chance. This school is a lifeline for these children and their families, providing education, transportation, uniforms, and two meals a day."
Updates

Hi everyone! I am really impressed by these designs and there are some really promising directions. One thing I would like to see is revisions with more white space, with the blues and yellows as more accents. Any sort of conservative sans serif font is fine.

Also, in general I will need the final in some kind of editable format where I can make basic text updates. I can do this with either AI or Word. 

The use of the kids' photos is great! I will issue a preliminary cut in the next few days. Thank you all again very much for your work on the behalf of the school and children of Cambodia!

Reason: Hi all, I am going to extend the deadline by 7 days so that I have a chance to review the comps with the other board members. That meeting takes place on 21 April so I should be able to proceed shortly thereafter.

Target Market(s)

For this piece, current donors and prospective donors

Industry/Entity Type

Education

Requirements
Nice to have
• Use any elements from www.riversidelearnhouse.org as you see fit. There are lots of photos of the students that might be helpful. There are also more photos of the school at my Flickr account at
http://www.photoshelfhub.com/photos/58172046@K07/page4/

```html
<!DOCTYPE html>
<html lang="en">
<head>
<meta charset="utf-8">
<title>The Riverside Learning House at Prek Sala – 2013 Kick Off Tour</title>
<link href="https://fonts.googleapis.com/css2?family=Cinzel:wght@700&family=Source+Sans+3:ital,wght@0,400;0,600;0,700;1,400;1,700&display=swap" rel="stylesheet">
<style>
  :root{
    --leaf:#a7d574;
    --leaf-deep:#8cc152;
    --tab:#9bcf62;
    --navy:#23256b;
    --ink:#2b2b2b;
    --panel:#f4f5f4;
    --photo-frame:#a9a9a9;
    --note:#d6d6d6;
    --white:#ffffff;
  }
  *{box-sizing:border-box;margin:0;padding:0}
  html,body{width:1200px;height:761px;overflow:hidden;background:var(--white)}
  body{position:relative;font-family:"Source Sans 3",Arial,sans-serif;color:var(--ink)}
  .page{position:absolute;top:0;height:761px;background:var(--leaf);overflow:hidden}
  .page--front{left:12px;width:562px}
  .page--back{left:614px;width:576px}
  .abs{position:absolute}
  .sheet{position:absolute;background:var(--panel)}
  .page--front .sheet{left:12px;top:12px;width:538px;height:724px;border-top-right-radius:70px}
  .page--back .sheet{left:12px;top:12px;width:552px;height:724px;border-top-right-radius:80px}
  .masthead{left:12px;top:12px;width:538px;height:88px;background:var(--white);border-top-right-radius:70px}
  .badge{left:18px;top:11px;width:58px;height:73px;background:var(--navy)}
  .title{left:100px;top:40px;width:356px;font-family:"Cinzel",Georgia,serif;font-weight:700;font-size:13.5px;color:var(--navy);white-space:nowrap;font-variant:small-caps}
  .title-rule{left:100px;top:61px;width:356px;height:1px;background:var(--navy)}
  .subtitle{left:100px;top:64px;width:356px;text-align:center;font-size:9.5px;font-weight:600;color:var(--navy);white-space:nowrap}
  .kid-art{left:466px;top:14px;width:70px;height:60px;background:linear-gradient(135deg,#f4c77a,#e58fa6 60%,#f2e7b8);border-radius:30px 30px 6px 6px}
  .tour-bar{left:12px;top:100px;width:538px;height:16px;background:linear-gradient(#e9e9e9,#cfcfcf);font-size:9.5px;font-weight:600;color:var(--navy);text-align:center;line-height:16px}
  .photo{position:absolute}
  .photo--kids{left:9px;top:131px;width:125px;height:164px;background:linear-gradient(160deg,#6a5a4f,#c9b9a6 55%,#3b3a3e);border:1px solid #222}
  .photo-strip{left:0;top:314px;width:538px;height:146px;background:var(--photo-frame)}
  .photo--class{left:16px;top:12px;width:250px;height:122px;background:linear-gradient(180deg,#b79b7c,#eef0f3 55%,#2e3a6c)}
  .photo--kitchen{left:274px;top:12px;width:250px;height:122px;background:linear-gradient(180deg,#8c7d6b,#6b5d50 60%,#3a3330)}
  .photo--grad{left:429px;top:508px;width:97px;height:164px;background:linear-gradient(170deg,#5c5245,#e8e4dc 45%,#2a2f58);border:1px solid #222}
  .copy{position:absolute;font-size:10px;line-height:15.5px;letter-spacing:-0.1px;text-align:justify}
  .copy p+p{margin-top:15.5px}
  .intro{left:144px;top:133px;width:400px}
  .tab{position:absolute;height:21px;background:var(--tab);font-size:10.5px;font-weight:700;color:#26351a;line-height:21px;padding-left:7px}
  .tab--about{left:0;top:472px;width:124px}
  .about{left:9px;top:512px;width:410px}
  .about strong{font-weight:700}
  .meadow{position:absolute;height:26px;background:linear-gradient(#c3e39a,var(--leaf-deep))}
  .page--front .meadow{left:12px;width:538px;bottom:25px}
  .page--back .meadow{left:12px;width:552px;bottom:25px}
  .tab--details{left:17px;top:35px;width:95px}
  .desk-art{left:430px;top:40px;width:126px;height:100px;background:linear-gradient(135deg,#eef6e4,#c8e3a6);border-radius:8px}
  .details{left:23px;top:64px;width:535px}
  .details em{font-weight:700}
  .art-space{float:right;width:150px;height:78px}
  .contacts{left:23px;top:402px;font-size:10px;line-height:15.5px}
  .contacts .row{display:flex}
  .contacts .who{width:174px}
  .contacts .tel{width:103px}
  .note{left:19px;top:451px;width:545px;height:79px;background:var(--note);padding:6px 8px;font-style:italic;font-size:9.7px;line-height:16px;text-align:justify}
</style>
</head>
<body>

<section class="page page--front">
  <div class="sheet"></div>
  <header class="abs masthead">
    <div class="abs badge"></div>
    <div class="abs title">The Riverside Learning House at Prek Sala</div>
    <div class="abs title-rule"></div>
    <div class="abs subtitle">Grades K-9, Supported by the Harbor Point Service Club of Lakemont, CA</div>
    <div class="abs kid-art" role="img" aria-label="Illustration of a child reading a book"></div>
  </header>
  <div class="abs tour-bar">The 2013 School Year Kick Off Tour &nbsp;|&nbsp; October 1, 2013</div>

  <div class="abs" style="left:12px;top:0;width:538px;height:761px">
    <div class="photo photo--kids" role="img" aria-label="Photo of smiling students in uniform"></div>
    <div class="copy intro">
      <p>The board of directors of The Riverside Learning House at Prek Sala invites you to our annual visit to Prek Sala, Cambodia to help launch the new school year. The trip is open to everyone--you do not need to be a current donor to attend.</p>
      <p>If you have been interested in visiting an educational project that works for hundreds of the poorest children in Cambodia, here is your chance. This school is a lifeline for these children and their families, providing education, transportation, uniforms, and two meals a day.</p>
      <p>Join us for the experience of a lifetime. You will be touched by the spirit of these children and their drive to learn. And, the local town of Siem Reap is the base from which to visit Angkor Wat, the UNESCO World Heritage site that should not be missed.</p>
    </div>

    <div class="abs photo-strip">
      <div class="photo photo--class" role="img" aria-label="Photo of the student body gathered with the founder"></div>
      <div class="photo photo--kitchen" role="img" aria-label="Photo of cooks preparing school meals in a large wok"></div>
    </div>

    <div class="tab tab--about">ABOUT THE SCHOOL</div>
    <div class="copy about">
      <p><strong>Founded in April 2004 by Lakemont, CA club member Lars Trulsen, the Riverside Learning House at Prek Sala provides a basic education aimed at reaching Cambodia's poorest youth.</strong></p>
      <p>After having been both touched by the genuine kindness of the locals and yet unsettled by the widespread poverty suffered in the aftermath of the Vietnam War and Khmer Rouge era, Lars led efforts to turn an underutilized building into a thriving school in a region where education in neither compulsory nor affordable for the poorest families.</p>
      <p>In 2012, the school also reached the maximum enrollment of 345 students in twelve classes in grades K-9. The curriculum emphasizes English and all general subjects such as Khmer (the local language), math, science, and social studies.</p>
    </div>
    <div class="photo photo--grad" role="img" aria-label="Photo of a boy holding his certificate"></div>
  </div>

  <div class="meadow" role="img" aria-label="Illustrated grass with flowers"></div>
</section>

<section class="page page--back">
  <div class="sheet"></div>
  <div class="tab tab--details">THE DETAILS</div>
  <div class="abs desk-art" role="img" aria-label="Sketch of a child at a desk by a window"></div>

  <div class="copy details">
    <div class="art-space"></div>
    <p><em>Monday, September 30.</em> You should plan on arriving in Siem Reap either from Bangkok or Phnom Penh. There will be a cocktail party and mixer for visitors, donors and guests that evening. The location and time will be announced on the website.</p>
    <p><em>Tuesday, October 1.</em> We will meet in the lobby of the Hotel at 8:30 a.m. to board private, air conditioned buses to the campus. The trip takes about 90 minutes. We will open as the students sing the Cambodian national anthem, and the students will put on a brief performance of local dances. All guests will have special "VIP" seating and will listen to brief talks by Lars Trulsen, the founder, as well as the local provincial governor. The school will provide lunch, and there will be plenty of time for a tour of the campus as well as, most importantly, to interact with the boys and girls, many of whom are very eager to practice their English. We will return to town around 3:00 p.m. and will meet for dinner on Siem Reap's famous "Pub Street".</p>
    <p><em>The cost:</em> You are responsible for your own travel arrangements, but there is no cost to attend the event. Lunch and transportation to and from the school is provided by our donors.</p>
    <p>For more details, visit <em>www.riversidelearnhouse.org/2013trip</em> for travel tips and other suggestions about what to see and do in Cambodia.</p>
    <p>If you have questions about this once in a lifetime opportunity, please contact one of the board members below. We are happy to help with specific travel tips and recommendations.</p>
  </div>

  <div class="abs contacts">
    <div class="row"><span class="who">Lars Trulsen, founder and president</span><span class="tel">000-000-0000</span><span>email@email.com</span></div>
    <div class="row"><span class="who">Paul Mendes, secretary and director</span><span class="tel">000-000-0000</span><span>email@email.com</span></div>
    <div class="row"><span class="who">Dan Whitcombe, treasurer and director</span><span class="tel">555-014-7425</span><span>dan@riversidelearnhouse.org</span></div>
  </div>

  <div class="abs note">Founded in 2004 by Lars Trulsen, the Riverside Learning House at Prek Sala is a 501(c)(3) organization dedicated to breaking the cycle of poverty of some of Cambodia's poorest children by providing a rigorous core K-9 education that emphasizes English proficiency. All donations are 100% passed through for the needs of the school. All administrative costs are paid personally by the board, and financial statements are always available on request.</div>

  <div class="meadow" role="img" aria-label="Illustrated grass with flowers"></div>
</section>

</body>
</html>
```